Zielgruppe
Ich biete die neue Dienstleistung an, Schulungen zu überprüfen auf deren Inhalt und mittels einem Zertifikat zu bestätigen, dass die geprüfte Schulung allen notwendigen Anforderungen der Normen und Regelwerke in Sachen Gaswarntechnik entspricht.
Daraufhin darf der Geprüfte (Schulungsanbieter/Schulungsgesellschaften) mit meinem Siegel für seine Schulumng werben.
Dies wird ausschießlich für Schulungen von Gaswarntechnik angeboten von mir angeboten. Das Siegel existiert schon und das Zertifikat sollte hier mit integriert werden.
Aufgabenstellung
Ich stelle mir ein hochwertiges Design vor, eine einzige DIN A4 Seite und 3D-Effekt. Es muss richtig teuer, hochwertig und modern aussehen, sodass man auch fühlt, dass es eine Wertigkeit hat. Das bestehende Siegel sollte integriert werden.
Ich brauche Textteile die ich anpassen kann. Zum einen muss ein Bereich da sein wo ich die Bezeichnung der geprüften Schulungen unterbringen kann, dann ein Bereich wo ich etwas zum Inhalt/Prüfung schreiben kann und natürlich Datum und Unterschriftsfeld. Das Zertifikat hat immer eine Gültigkeit von 2 Jahren ab Ausstellungsdatum.
Es sollten meine Farben eingsetzt werden. Zum einen ist dies
Ultramarinblau RAL 5002 RGB= rot 0/grün 56/ blau 123
Weiß
gelb (nicht genau definiert), rapsgelb RAL 1021/1023
Schriftart Verdana
Das Design sollte an mein bestehndes Design in Sachen Logo/Homepage angelehnt sein.

```html
<!DOCTYPE html>
<html lang="de">
<head>
<meta charset="utf-8">
<title>Zertifikat – Hoch- und Querformat</title>
<link href="https://fonts.googleapis.com/css2?family=Playfair+Display:wght@500&family=Montserrat:wght@400;700&family=Courgette&family=Dancing+Script:wght@700&display=swap" rel="stylesheet">
<style>
  :root {
    --backdrop: #e6e6e6;
    --paper: #ffffff;
    --ultramarine: #00387b;
    --ultramarine-light: #1f6fb8;
    --rapeseed: #eda615;
    --rapeseed-deep: #d98c0a;
    --name-gold: #d9993a;
    --ink: #1d1d1d;
    --body-ink: #333333;
  }
  * { box-sizing: border-box; margin: 0; padding: 0; }
  html, body { width: 1200px; height: 687px; overflow: hidden; }
  body { background: var(--backdrop); position: relative; font-family: "Montserrat", sans-serif; color: var(--ink); }

  .certificate { position: absolute; background: var(--paper); overflow: hidden; }
  .certificate--portrait { left: 66px; top: 52px; width: 439px; height: 571px; }
  .certificate--landscape { left: 555px; top: 209px; width: 579px; height: 414px; }

  .certificate__frame { position: absolute; inset: 12px; border: 1px solid var(--rapeseed); }

  .corner { position: absolute; width: 240px; height: 160px; }
  .corner--top-left { left: 0; top: 0; }
  .corner--bottom-right { right: 0; bottom: 0; transform: rotate(180deg); }

  .seal { position: absolute; border-radius: 4px; background: var(--rapeseed); }
  .certificate--portrait .seal { left: 186px; top: 38px; width: 66px; height: 90px; }
  .certificate--landscape .seal { left: 472px; top: 34px; width: 66px; height: 90px; }

  .certificate__content { position: absolute; left: 0; right: 0; text-align: center; }
  .certificate__title {
    font-family: "Playfair Display", serif; font-weight: 500;
    font-size: 31px; letter-spacing: 3px; color: var(--ink);
  }
  .certificate__rule { width: 132px; height: 1px; background: var(--ink); margin: 6px auto 0; }
  .certificate__issued { font-size: 8.5px; font-weight: 700; letter-spacing: 1.5px; margin-top: 14px; }
  .certificate__recipient { font-family: "Courgette", cursive; font-size: 34px; color: var(--name-gold); line-height: 1.2; }
  .certificate__stars { color: var(--rapeseed); font-size: 15px; letter-spacing: 3px; }
  .certificate__text { font-size: 8.5px; line-height: 1.55; color: var(--body-ink); margin-left: auto; margin-right: auto; }

  .certificate__date { position: absolute; font-size: 8.5px; font-weight: 700; letter-spacing: 1.5px; }
  .certificate__signature { position: absolute; font-family: "Dancing Script", cursive; font-weight: 700; font-size: 22px; color: var(--ultramarine); }

  .certificate--portrait .certificate__content { top: 180px; }
  .certificate--portrait .certificate__recipient { margin-top: 26px; }
  .certificate--portrait .certificate__stars { margin-top: 12px; }
  .certificate--portrait .certificate__text { width: 270px; margin-top: 18px; }
  .certificate--portrait .certificate__date { left: 0; right: 0; text-align: center; top: 452px; }
  .certificate--portrait .certificate__signature { left: 66px; top: 500px; }

  .certificate--landscape .certificate__content { top: 84px; }
  .certificate--landscape .certificate__recipient { margin-top: 12px; }
  .certificate--landscape .certificate__stars { margin-top: 8px; }
  .certificate--landscape .certificate__text { width: 290px; margin-top: 18px; }
  .certificate--landscape .certificate__date { left: 86px; top: 350px; }
  .certificate--landscape .certificate__signature { left: 150px; top: 336px; }
</style>
</head>
<body>

<svg width="0" height="0" style="position:absolute">
  <defs>
    <linearGradient id="band-blue" x1="0" y1="0" x2="1" y2="1">
      <stop offset="0" stop-color="#00387b"/>
      <stop offset="1" stop-color="#1f6fb8"/>
    </linearGradient>
    <linearGradient id="band-gold" x1="0" y1="0" x2="1" y2="1">
      <stop offset="0" stop-color="#f5b52a"/>
      <stop offset="1" stop-color="#d98c0a"/>
    </linearGradient>
    <symbol id="corner-bands" viewBox="0 0 240 160">
      <polygon points="0,0 180,0 0,112" fill="url(#band-blue)"/>
      <polygon points="60,0 150,0 0,95 0,38" fill="#0b4f98" opacity="0.55"/>
      <polygon points="190,0 232,0 0,146 0,120" fill="url(#band-gold)"/>
    </symbol>
  </defs>
</svg>

<section class="certificate certificate--portrait">
  <svg class="corner corner--top-left"><use href="#corner-bands"/></svg>
  <svg class="corner corner--bottom-right"><use href="#corner-bands"/></svg>
  <div class="certificate__frame"></div>
  <div class="seal" role="img" aria-label="Prüfsiegel"></div>

  <div class="certificate__content">
    <h1 class="certificate__title">ZERTIFIKAT</h1>
    <div class="certificate__rule"></div>
    <p class="certificate__issued">AUSGESTELLT AN</p>
    <p class="certificate__recipient">Name Nachname</p>
    <p class="certificate__stars">★★★★★</p>
    <p class="certificate__text">Lorem ipsum dolor sit amet, consectetuer adipiscing elit, sed diam nonummy nibh euismod tincidunt ut laoreet dolore magna aliquam erat volutpat. Ut wisi</p>
  </div>
  <p class="certificate__date">DATUM</p>
  <p class="certificate__signature">Unterschrift</p>
</section>

<section class="certificate certificate--landscape">
  <svg class="corner corner--top-left"><use href="#corner-bands"/></svg>
  <svg class="corner corner--bottom-right"><use href="#corner-bands"/></svg>
  <div class="certificate__frame"></div>
  <div class="seal" role="img" aria-label="Prüfsiegel"></div>

  <div class="certificate__content">
    <h1 class="certificate__title">ZERTIFIKAT</h1>
    <div class="certificate__rule"></div>
    <p class="certificate__issued">AUSGESTELLT AN</p>
    <p class="certificate__recipient">Name Nachname</p>
    <p class="certificate__stars">★★★★★</p>
    <p class="certificate__text">Lorem ipsum dolor sit amet, consectetuer adipiscing elit, sed diam nonummy nibh euismod tincidunt ut laoreet dolore magna aliquam erat volutpat. Ut wisi</p>
  </div>
  <p class="certificate__date">DATUM</p>
  <p class="certificate__signature">Unterschrift</p>
</section>

</body>
</html>
```